Geschäftspapiere für Handwerksunternehmen
Zielgruppe
Handwerk
Elektroinstallation
Design Modern
Aufgabenstellung
Anschrift, Kontaktdaten, Bankverbindung, Logo,
Im Lindengrund 7 47391 Salem Inhaber Jonas Velbrück
Telefon: 04128-6350712 Email: info@trolvane-elektrotechnik.de Internet: www.trolvane-elektrotechnik.de
Finanzamt Hobrachtal USt.-ID: DE574036218 Steuer Nr.:3196450721
Kreiskasse Wendorn IBAN:DE71430982160004197356 BIC:WKRNDEF1WDN

```html
<!DOCTYPE html>
<html lang="de">
<head>
<meta charset="utf-8">
<title>Trolvane Elektrotechnik – Geschäftspapiere</title>
<link rel="stylesheet" href="https://fonts.googleapis.com/css2?family=Open+Sans:wght@400;600;700&display=swap">
<style>
:root{
  --bg:#e2e3e7;
  --paper:#f3f4f6;
  --white:#ffffff;
  --ink:#0a0b0b;
  --yellow:#e6e41b;
  --grey:#6f7073;
  --lightgrey:#9a9b9e;
}
*{margin:0;padding:0;box-sizing:border-box}
html,body{width:1200px;height:936px;overflow:hidden}
body{background:var(--bg);font-family:"Open Sans",Arial,sans-serif;position:relative;color:var(--ink)}
.piece{position:absolute}

/* brand mark: plain circle + name */
.mark{display:flex;align-items:center;gap:.35em;color:var(--yellow);font-weight:700;letter-spacing:.08em;white-space:nowrap}
.mark .dot{width:.9em;height:.9em;border-radius:50%;background:var(--yellow);flex:none}
.mark.dark{color:var(--ink)}
.mark.dark .dot{background:var(--yellow)}

/* business card front */
.card-front{left:140px;top:194px;width:180px;height:104px;background:var(--white)}
.card-front .mark{position:absolute;left:-8px;top:46px;font-size:10px;transform:rotate(-90deg);transform-origin:center;width:70px;justify-content:center}
.card-front .rule{position:absolute;left:55px;top:30px;width:1px;height:40px;background:var(--ink)}
.card-front .info{position:absolute;left:60px;top:31px;font-size:5px;line-height:1.35}
.card-front .name{font-weight:700;font-size:5.6px;text-transform:uppercase}
.card-front .name span{color:var(--yellow)}
.card-front .role{font-weight:600;margin-bottom:4px}
.card-front .line{display:flex;align-items:center;gap:3px;font-weight:600}
.card-front .line i{width:3px;height:3px;border-radius:50%;background:var(--yellow);display:block}

/* business card back */
.card-back{left:140px;top:345px;width:179px;height:105px;background:var(--ink);display:flex;align-items:center;justify-content:center}
.card-back .mark{font-size:13px}

/* letterhead */
.letter{left:388px;top:188px;width:348px;height:493px;background:var(--paper);color:var(--grey)}
.letter .mark{position:absolute;left:26px;top:67px;font-size:14px}
.letter .date{position:absolute;left:27px;top:134px;font-size:8px;letter-spacing:.08em}
.letter .body{position:absolute;left:27px;top:170px;width:292px;font-size:7.6px;line-height:9.4px;letter-spacing:.06em;text-align:justify}
.letter .body p+p{margin-top:9px}
.letter .signature{position:absolute;right:29px;top:348px;font-size:7.6px;letter-spacing:.08em}
.letter .footer{position:absolute;right:27px;top:438px;font-size:4.6px;line-height:6.6px;text-align:right}
.letter .footer b{color:var(--yellow);font-weight:400}
.letter .tab{position:absolute;right:0;top:439px;width:11px;height:18px;background:var(--yellow)}

/* DL envelope */
.envelope-dl{left:794px;top:210px;width:357px;height:181px;background:var(--ink);color:var(--white)}
.envelope-dl .mark{position:absolute;left:31px;top:42px;font-size:11px}
.envelope-dl .address{position:absolute;left:26px;top:110px;font-size:4.8px;line-height:6.4px}
.envelope-dl .address hr{border:0;height:1px;width:66px;background:var(--yellow);margin:3px 0 4px}

/* folder */
.folder{left:802px;top:414px;width:356px;height:471px;background:var(--ink);display:flex;align-items:center;justify-content:center}
.folder .mark{font-size:30px;margin-top:42px;margin-left:90px}

/* bottom envelope */
.envelope{left:386px;top:705px;width:354px;height:180px;background:var(--paper);overflow:hidden}
.envelope .flap{position:absolute;left:0;top:0;width:354px;height:48px;background:var(--ink);border-radius:0 0 16px 16px}
.envelope .mark{position:absolute;left:0;right:0;top:14px;justify-content:center;font-size:11px}
</style>
</head>
<body>

<section class="piece card-front" aria-label="Visitenkarte Vorderseite">
  <div class="mark dark"><span class="dot"></span><span>TROLVANE</span></div>
  <div class="rule"></div>
  <div class="info">
    <div class="name">Jonas <span>Velbrück</span></div>
    <div class="role">Inhaber</div>
    <div class="line"><i></i>04128-6350712</div>
    <div class="line"><i></i>info@trolvane-elektrotechnik.de</div>
    <div class="line"><i></i>www.trolvane-elektrotechnik.de</div>
    <div class="line"><i></i>Im Lindengrund 7, 47391 Salem</div>
  </div>
</section>

<section class="piece card-back" aria-label="Visitenkarte Rückseite">
  <div class="mark"><span class="dot"></span><span>TROLVANE</span></div>
</section>

<section class="piece letter" aria-label="Briefbogen">
  <div class="mark"><span class="dot"></span><span class="name" style="color:var(--ink)">TROLVANE</span></div>
  <div class="date">Sep 27, 2019</div>
  <div class="body">
    <p>Sep 27, 2019 (Marktbericht Nordhaven) -- Eine neue Studie zur Elektroinstallation in Wohn- und Gewerbebauten wurde veröffentlicht. Sie enthält über 100 Tabellen, Diagramme und Kennzahlen und bietet eine vollständige Bewertung des Marktes, aktueller Entwicklungen, Szenarien und Wachstumsfaktoren. Die Studie liefert geprüfte Marktdaten und eine Aufschlüsselung nach</p>
    <p>Umsatz und Volumen sowie historische Preisentwicklungen für die Region. Einige der führenden Installationsbetriebe der Region sind Teil der Untersuchung, ebenso Planungsbüros, Großhändler, Stadtwerke und Netzbetreiber aus dem Umland sowie Fachverbände.
    Erfahren Sie mehr über Vor- und Nachteile der geltenden Vorschriften der Bran</p>
  </div>
  <div class="signature">SIGNATURE</div>
  <div class="footer">
    Finanzamt Hobrachtal <b>|</b> USt-ID: DE574036218<br>
    IBAN: DE71430982160004197356 <b>|</b> BIC: WKRNDEF1WDN<br>
    Kreiskasse Wendorn / Steuer-Nr. 3196450721
  </div>
  <div class="tab"></div>
</section>

<section class="piece envelope-dl" aria-label="Briefumschlag DIN lang">
  <div class="mark"><span class="dot"></span><span>TROLVANE</span></div>
  <div class="address">
    Im Lindengrund 7<br>47391 Salem
    <hr>
    Tel: 04128-6350712<br>
    Email: info@trolvane-elektrotechnik.de<br>
    Website: www.trolvane-elektrotechnik.de
  </div>
</section>

<section class="piece folder" aria-label="Präsentationsmappe">
  <div class="mark"><span class="dot"></span><span>TROLVANE</span></div>
</section>

<section class="piece envelope" aria-label="Briefumschlag">
  <div class="flap"></div>
  <div class="mark"><span class="dot"></span><span>TROLVANE</span></div>
</section>

</body>
</html>
```